依頼詳細
拠点周辺での新規顧客の獲得及び新拠点の営業開始の為、新聞折込を計画しており、新聞折込用のチラシ製作をお願い致します。お手入れできていないお庭をなんとかしたい!と思っている方、ご自分でお手入れしているもののやはりプロに頼みたい!と思っている方の目に留まるデザインを希望しております。ご相談を受け、現地で状態をしっかり確認した後ご提案、お見積りさせて頂く為、価格や料金プランはございません。また、新拠点の営業期間は当面3月〜5月の予定です。
記載項目
社  名:樋口庭苑
営業拠点:長野本店、茅野新店※3月〜5月
受付時間:9:30〜18:30 ※年中無休
電話番号:026-318-4452
(携帯 :090-7723-6041)
E- m a i l:info@hgchteien-example.com
本店住所:長野市若葉台西2丁目4-7 コーポ白樺105
サイズ
A4
ページ数
片面
希望イメージ
シンプル 複雑
単色 カラフル
暗い 明るい
日常 高級
遊び心 厳粛
未来的 伝統的
女性的 男性的
希望する色
緑系、水色系
納品ファイル
• 高解像度JPG (.jpg)
補足説明
◾️依頼タイトル変更
◾️施工例などの写真は使用しません。
一目で『業者のチラシ』と分かるものとは一線を画し、
「これ植木屋さん?!」と意表を突くデザイン性に富んだチラシを求めております。
抽象的で申し訳ないのですが、お力添えをお願い致します。

◾️記載項目の事業者情報の他、下記の記載をお願い致します。
・グリーンアドバイザーがお庭をなんとかしたい方のお悩みに丁寧にお応えする、という趣旨
・ご相談、お見積りは無料であること
・茅野市(長野県)で営業を開始すること※営業期間は3月から5月
◾️他社様ですが、素人なりに製作した過去のサンプルを添付しました。
*誠に申し訳ございませんが、
『概要・特徴』の内容を誤っておりました。
1級技能士と記載しておりますが、
造園関連ではございませんでした。
本当に申し訳ございません。
ご迷惑をおかけいたしますが、
記載項目からは外していただきますよう、
何卒お願い申し上げます。
■新聞折込は長野市内の部数を多めに予定しておりますので、
茅野新店についての記載は目立つ配置でなくて良いです。
*ご提案いただける方の制限につきまして、
訂正させていただいております。
多くの皆様のご提案をお待ちしております!
*前回同様
■ 選んだ理由

これ、植木屋さんなんだー!と驚くなんとも清潔感のある斬新さと、読みやすく分かりやすいシンプルさがとても印象的で、この度選ばせて頂きました。

■ 提案者全員のお礼・コメント

この度は、当方のご依頼にこのように多くの皆様にご提案をいただき、ただただ感謝申し上げます。利用させていただくのが初めてで、ご説明不足や当方の不手際等で大変お手数をおかけしてしまったにも関わらず、皆様のご対応の迅速さに、脱帽でした。本当に、有難うございました。

```html
<!DOCTYPE html>
<html lang="ja">
<head>
<meta charset="utf-8">
<title>樋口庭苑 グリーンアドバイザー</title>
<link href="https://fonts.googleapis.com/css2?family=Great+Vibes&family=M+PLUS+Rounded+1c:wght@500;700;800&family=Noto+Sans+JP:wght@400;500;700&display=swap" rel="stylesheet">
<style>
:root{
  --sky-top:#3f95d6;
  --sky-mid:#7bbbe8;
  --cloud:#dcecf6;
  --garden-dark:#2f5a2a;
  --garden-mid:#4d7e3a;
  --path:#cfc6b0;
  --white:#ffffff;
  --blue:#2d86c9;
  --green:#3c9a3c;
  --lime:#8dbb2a;
  --ink:#3a3a3a;
  --muted:#666;
}
*{margin:0;padding:0;box-sizing:border-box}
html,body{width:851px;height:1200px;overflow:hidden;background:var(--white)}
body{font-family:"Noto Sans JP",sans-serif;color:var(--ink)}
.flyer{position:relative;width:851px;height:1200px;overflow:hidden;background:var(--white)}
.scene{position:absolute;left:0;top:0;width:851px;height:1100px;
  background:linear-gradient(180deg,var(--sky-top) 0%,var(--sky-mid) 38%,var(--cloud) 58%,var(--garden-mid) 72%,var(--garden-dark) 84%,var(--path) 100%);}
.script{position:absolute;left:380px;top:48px;font-family:"Great Vibes",cursive;font-size:62px;color:rgba(255,255,255,.9);transform:rotate(-12deg);white-space:nowrap}
.title{position:absolute;left:96px;top:128px;font-family:"M PLUS Rounded 1c",sans-serif;font-weight:800;color:var(--white);font-size:104px;line-height:136px;letter-spacing:0;white-space:nowrap;text-shadow:0 2px 8px rgba(0,60,120,.25)}
.badge{position:absolute;left:646px;top:116px;width:168px;height:168px;border-radius:50%;background:var(--white);color:var(--blue);text-align:center;display:flex;flex-direction:column;justify-content:center;font-weight:700}
.badge .small{font-size:21px;line-height:27px}
.badge .big{font-size:38px;line-height:48px;font-weight:700}
.lead{position:absolute;left:120px;width:611px;top:488px;padding:8px 0;border-top:2px solid var(--white);border-bottom:2px solid var(--white);text-align:center;color:var(--white);font-size:30px;font-weight:500;letter-spacing:1px;white-space:nowrap}
.body-copy{position:absolute;left:0;width:851px;top:568px;text-align:center;color:var(--white);font-size:25px;line-height:40px;font-weight:500;text-shadow:0 1px 4px rgba(0,50,100,.35)}
.branch{position:absolute;left:16px;top:1014px;width:262px;padding:8px 12px;background:rgba(255,255,255,.92);color:var(--lime);font-weight:700;font-size:17px;line-height:24px;white-space:nowrap}
.branch .period{display:inline-block;font-size:12px;line-height:17px;border:1px solid var(--lime);padding:0 6px;margin-top:3px;color:var(--lime)}
.footer{position:absolute;left:0;top:1100px;width:851px;height:100px;display:flex;align-items:center;padding:0 14px;gap:14px}
.call{flex:0 0 128px;height:56px;border:2px solid var(--green);color:var(--green);font-size:13px;line-height:19px;font-weight:700;display:flex;align-items:center;justify-content:center;text-align:center}
.brand{flex:0 0 280px;white-space:nowrap}
.brand .roman{font-size:10px;letter-spacing:3px;color:var(--green)}
.brand .name{font-size:30px;font-weight:700;color:var(--green);line-height:36px}
.brand .addr{font-size:10px;color:var(--muted)}
.contact{flex:1;color:var(--green);white-space:nowrap;min-width:0}
.contact .tel{display:flex;align-items:baseline;gap:8px}
.contact .tel b{font-size:28px;font-weight:700;line-height:34px}
.contact .hours{font-size:10px;color:var(--muted)}
.contact .sub{display:flex;flex-direction:column;gap:2px;font-size:13px;color:var(--ink);margin-top:4px}
.contact .sub span{display:flex;align-items:center;gap:5px}
</style>
</head>
<body>
<div class="flyer">
  <div class="scene" role="img" aria-label="青空と白い雲の下に、石垣と庭木に囲まれた明るい庭、テーブルと椅子が置かれたテラスの写真"></div>

  <div class="script">Green Adviser</div>
  <h1 class="title">グリーン<br>アドバイザー</h1>

  <div class="badge">
    <span class="small">ご相談</span>
    <span class="small">お見積り</span>
    <span class="big">無料</span>
  </div>

  <p class="lead">お庭の事、何でもご相談ください</p>
  <p class="body-copy">一つ一つの庭木の状態を丁寧に確認し、<br>適切なご提案、お見積りをいたします。</p>

  <div class="branch">
    茅野市にて営業開始しました<br>
    <span class="period">営業期間：3月〜5月</span>
  </div>

  <footer class="footer">
    <div class="call">まずはお電話で<br>ご相談ください</div>
    <div class="brand">
      <div class="roman">HIGUCHI TEIEN</div>
      <div class="name">樋口庭苑</div>
      <div class="addr">長野市若葉台西2丁目4-7 コーポ白樺105</div>
    </div>
    <div class="contact">
      <div class="tel">
        <b>tel.026-318-4452</b>
        <span class="hours">受付 9:30〜18:30（年中無休）</span>
      </div>
      <div class="sub">
        <span>
          <svg width="13" height="13" viewBox="0 0 24 24" aria-hidden="true"><path fill="#3c9a3c" d="M6.6 10.8a15 15 0 0 0 6.6 6.6l2.2-2.2a1 1 0 0 1 1-.25 11.4 11.4 0 0 0 3.6.57 1 1 0 0 1 1 1V20a1 1 0 0 1-1 1A17 17 0 0 1 3 4a1 1 0 0 1 1-1h3.5a1 1 0 0 1 1 1c0 1.25.2 2.45.57 3.57a1 1 0 0 1-.25 1z"/></svg>
          090-7723-6041
        </span>
        <span>
          <svg width="13" height="13" viewBox="0 0 24 24" aria-hidden="true"><rect x="2" y="5" width="20" height="14" rx="2" fill="none" stroke="#3c9a3c" stroke-width="2"/><path d="M3 6l9 7 9-7" fill="none" stroke="#3c9a3c" stroke-width="2"/></svg>
          info@hgchteien-example.com
        </span>
      </div>
    </div>
  </footer>
</div>
</body>
</html>
```